I am medical doctor in surgery specialized in Urology and anti-aging. I need Web and Instagram design for a head cream , face cream and body lotion. I did a 2% GHK-Cu solution (head-face-body) with an professional pharmacist specialized in manufacturing creams. . GHK-Cu is a tri-peptide with solid scientific background to rejuvenate the skin (will stimulate collagen production) and can promote hair regrowth. Statistically 70% of peptides bought are fake on the market, I can personally guarantee about purity (my peptides are certified pure above 99% checked in an independent laboratory in London -UK.
I want to use the name 'Lunavel'. I secured already the domain names. I had an design for another project I could re-use for this project. The ribbon should include more blue. The font of Lunavel can be changed. I got a logo which is ok for me. Web design best coded with Wordpress.

Target Market(s)

Anti aging, skin care, hair regrowth, skin collagen

Industry/Entity Type

the cream can also be used after surgery for faster and better wound healing

Number of Pages Required

5+ page

Font styles to use
Sans Serif

Colors
0054AA
0677BA
7BADD7
CADEEF
E8F1F8

Requirements
Must have
• target population 30-70 years
Nice to have
• scientific proof, pictures before-after
Should not have
• GHK-Cu has solid scientific animal studies of anti-cancer properties. It is 100% safe for dermal human use.

```html
<!DOCTYPE html>
<html lang="en">
<head>
<meta charset="utf-8">
<title>Lunavel — Advanced Peptide Skincare</title>
<link href="https://fonts.googleapis.com/css2?family=Jost:wght@400;500;600&family=Source+Serif+4:ital,opsz,wght@0,8..60,600;1,8..60,500&display=swap" rel="stylesheet">
<style>
  :root{
    --brand:#0054AA;
    --brand-mid:#0677BA;
    --brand-soft:#7BADD7;
    --mist:#CADEEF;
    --ice:#E8F1F8;
    --ink:#0E1433;
    --text:#2A3150;
    --white:#ffffff;
  }
  *{margin:0;padding:0;box-sizing:border-box}
  html,body{width:1200px;height:802px;overflow:hidden}
  body{
    position:relative;
    background:linear-gradient(160deg,#ffffff 0%,#f6f9fd 45%,var(--ice) 100%);
    font-family:"Jost",sans-serif;color:var(--text);
  }
  .hero-visual{
    position:absolute;left:470px;top:110px;width:730px;height:692px;
    background:
      radial-gradient(ellipse 55% 40% at 60% 48%,rgba(255,255,255,.95) 0%,rgba(255,255,255,0) 70%),
      linear-gradient(160deg,var(--ice) 0%,var(--mist) 45%,var(--brand-soft) 75%,var(--brand-mid) 100%);
    border-radius:40px 0 0 0;
    opacity:.85;
  }
  .site-header{
    position:absolute;left:0;top:0;width:1200px;height:110px;
  }
  .nav-shell{
    position:absolute;left:300px;top:12px;width:930px;height:74px;
    background:rgba(255,255,255,.75);border-radius:37px;
  }
  .brand{
    position:absolute;left:62px;top:38px;display:flex;align-items:center;gap:10px;
    font-family:"Jost",sans-serif;font-weight:600;font-size:36px;color:var(--brand);
  }
  .brand-dot{width:22px;height:22px;border-radius:50%;background:var(--brand-mid)}
  .main-nav{position:absolute;top:52px;left:0;font-size:12.5px;color:var(--ink)}
  .main-nav a{position:absolute;white-space:nowrap;color:inherit;text-decoration:none}
  .nav-icon{position:absolute;top:50px}
  .btn{
    position:absolute;display:flex;align-items:center;justify-content:center;
    font-family:"Jost",sans-serif;text-decoration:none;border-radius:2px;
  }
  .btn-primary{background:var(--brand);color:var(--white)}
  .btn-outline{border:1.5px solid var(--brand);color:var(--brand);background:var(--white)}
  .header-cta{left:1062px;top:45px;width:84px;height:30px;font-size:12px;border-radius:3px}
  .eyebrow{
    position:absolute;left:66px;top:182px;font-size:11.5px;font-weight:500;
    letter-spacing:3.6px;color:var(--brand);
  }
  .headline{
    position:absolute;left:64px;top:206px;
    font-family:"Source Serif 4",serif;font-weight:600;font-size:63px;line-height:67px;
    color:var(--ink);letter-spacing:-.5px;
  }
  .headline em{font-weight:500;color:var(--brand-mid);font-style:italic}
  .lede{
    position:absolute;left:66px;top:358px;width:420px;font-size:15px;line-height:24.6px;color:var(--text);
  }
  .hero-cta{top:483px;height:40px;font-size:15px}
  .cta-shop{left:66px;width:142px}
  .cta-science{left:230px;width:175px}
  .purity-seal{position:absolute;left:126px;top:550px}
</style>
</head>
<body>
  <div class="hero-visual" role="img" aria-label="Product photo: head cream, face cream and body lotion bottles on a white podium with a flowing blue ribbon"></div>

  <header class="site-header">
    <div class="nav-shell"></div>
    <div class="brand"><span class="brand-dot"></span>Lunavel</div>
    <nav class="main-nav">
      <a style="left:333px">Home</a>
      <a style="left:391px">Products</a>
      <a style="left:467px">Why Lunavel?</a>
      <a style="left:574px">Science</a>
      <a style="left:650px">About Doctor</a>
      <a style="left:752px">Before &amp; After</a>
      <a style="left:860px">FAQ</a>
      <a style="left:906px">Contacts</a>
    </nav>
    <svg class="nav-icon" style="left:989px" width="16" height="18" viewBox="0 0 16 18" fill="none" stroke="#0E1433" stroke-width="1.3"><circle cx="8" cy="5.5" r="4"/><path d="M1 17c0-4 3-6 7-6s7 2 7 6"/></svg>
    <svg class="nav-icon" style="left:1026px" width="16" height="18" viewBox="0 0 16 18" fill="none" stroke="#0E1433" stroke-width="1.3"><rect x="1.5" y="5.5" width="13" height="11.5" rx="1"/><path d="M5 7V4a3 3 0 0 1 6 0v3"/></svg>
    <a class="btn btn-primary header-cta">Shop Now</a>
  </header>

  <main>
    <p class="eyebrow">SCIENCE. PURITY. REGENERATION.</p>
    <h1 class="headline">Advanced Peptide<br>Skincare <em>by Science</em></h1>
    <p class="lede">Lunavel harnesses the power of 99%+ pure GHK-Cu peptide to rejuvenate skin, stimulate hair regrowth, and enhance natural healing. Developed by a Medical Doctor and formulated with pharmaceutical precision.</p>
    <a class="btn btn-primary hero-cta cta-shop">Shop Now</a>
    <a class="btn btn-outline hero-cta cta-science">Explore the Science</a>
    <svg class="purity-seal" width="164" height="164" viewBox="0 0 164 164" aria-hidden="true">
      <circle cx="82" cy="82" r="80" fill="rgba(255,255,255,.8)" stroke="#7BADD7" stroke-width="1"/>
      <circle cx="82" cy="82" r="64" fill="none" stroke="#CADEEF" stroke-width="1"/>
    </svg>
  </main>
</body>
</html>
```